"Lantern Over Fields" Gospel Presentation Booklet

I need a design for a 12 page (including front/back cover) square booklet, with religious images and aesthetically pleasing fonts/designs. I want it to be very simple, and very straightforward. The main focus of the project is it's content. So the design should be very nice, but also should point to the content, not take away from it, or create distraction. People should be more focused on the words than the imagery.

I enjoy modern designs, I need a sharp aesthetic that is clean and neat. Nothing over the top.
I have attached a word document with the content I would like on the pages.

Colors
0592cd
0255a3
33a6d7
85cae6
85acd3
3276b5
9bcb3b
f04a50
f68d4c

Requirements
Should not have
• Super feminine colors/aesthetics

```html
<!DOCTYPE html>
<html lang="en">
<head>
<meta charset="utf-8">
<title>Lantern Over Fields – Booklet Spreads</title>
<link href="https://fonts.googleapis.com/css2?family=Oswald:wght@500;700&family=Raleway:wght@300;400;600&display=swap" rel="stylesheet">
<style>
  :root {
    --page: #ffffff;
    --sky-deep: #0255a3;
    --sky-mid: #3276b5;
    --sky-bright: #0592cd;
    --sky-light: #33a6d7;
    --sky-pale: #85cae6;
    --dusk: #85acd3;
    --panel-bg: #c9dcee;
    --panel-bg-light: #dbe8f4;
    --card-bg: #eef3fa;
    --frame: #3276b5;
    --ink: #1f5c9e;
  }
  * { box-sizing: border-box; margin: 0; padding: 0; }
  html, body { width: 1200px; height: 923px; overflow: hidden; background: var(--page); }
  .sheet {
    position: relative; width: 1200px; height: 923px;
    display: grid;
    grid-template-columns: 532px 532px;
    grid-template-rows: 266px 266px 266px;
    column-gap: 14px; row-gap: 18px;
    padding: 44px 62px;
  }
  .spread {
    position: relative; overflow: hidden;
    background: radial-gradient(ellipse at 30% 50%, var(--panel-bg-light), var(--panel-bg) 80%);
  }

  /* Cover */
  .cover { background: linear-gradient(180deg, #1b4f9c 0%, #2f78c4 35%, #7fb4e2 55%, #3b7cc6 70%, #1d56a0 100%); }
  .cover-photo { position: absolute; inset: 0;
    background: radial-gradient(ellipse at 55% 55%, rgba(255,255,255,.55), rgba(255,255,255,0) 45%); }
  .cover-title {
    position: absolute; left: 305px; top: 51px; width: 189px; height: 161px;
    border: 2px solid var(--sky-deep); outline: 1px solid var(--sky-deep); outline-offset: 3px;
    background: rgba(255,255,255,.35);
    display: flex; align-items: center; justify-content: center; text-align: center;
    font-family: "Oswald", sans-serif; font-weight: 700; color: var(--sky-deep);
    font-size: 34px; line-height: 1.02; text-transform: uppercase;
  }
  .cover-cross { position: absolute; left: 392px; top: 32px; }

  /* Interior spreads */
  .emblem {
    position: absolute; left: 16px; top: 18px; width: 230px; height: 230px; border-radius: 50%;
    background: radial-gradient(circle, #ffffff 0%, #ffffff 23%, #d6ecf8 30%, var(--sky-pale) 42%, rgba(51,166,215,.55) 55%, rgba(133,172,211,0) 71%);
  }
  .heading {
    position: absolute; left: 131px; top: 133px; transform: translate(-50%, -50%);
    font-family: "Oswald", sans-serif; font-weight: 700; text-transform: uppercase;
    color: var(--sky-bright); font-size: 44px; letter-spacing: .5px; white-space: nowrap;
    text-shadow: 0 0 6px #fff;
  }
  .heading.long { font-size: 42px; }
  .message {
    position: absolute; left: 295px; top: 31px; width: 206px; height: 203px;
    border: 2px solid var(--frame); outline: 1px solid var(--frame); outline-offset: -6px;
    background: linear-gradient(135deg, #ffffff, var(--card-bg) 60%, #d9e6f3);
    display: flex; flex-direction: column; justify-content: center; align-items: center;
    text-align: center; padding: 14px 18px;
    font-family: "Raleway", sans-serif; font-weight: 400; color: var(--ink);
  }
  .message p + p { margin-top: 12px; }
  .size-lg { font-size: 15.5px; line-height: 1.32; }
  .size-md { font-size: 12.5px; line-height: 1.3; }
  .size-sm { font-size: 12px; line-height: 1.28; }
  .steps { font-size: 7.4px; line-height: 1.3; padding: 10px 14px; }
  .steps p + p { margin-top: 7px; }
  .steps .call { font-weight: 600; font-size: 10.6px; line-height: 1.28; margin-top: 12px; }
</style>
</head>
<body>
<main class="sheet">

  <section class="spread cover">
    <div class="cover-photo" role="img" aria-label="Photograph of a person in prayer over a calm sea under a blue sky"></div>
    <svg class="cover-cross" width="16" height="22" viewBox="0 0 16 22" aria-hidden="true">
      <rect x="6.5" y="0" width="3" height="22" fill="#0255a3"/>
      <rect x="1" y="6" width="14" height="3" fill="#0255a3"/>
    </svg>
    <h1 class="cover-title">Lantern<br>Over<br>Fields</h1>
  </section>

  <section class="spread">
    <div class="emblem" role="img" aria-label="Radiant cross ornament"></div>
    <h2 class="heading">God</h2>
    <div class="message size-lg"><p>God is holy, that means He’s perfect. In fact, He is so perfect, corruption cannot live with Him.</p></div>
  </section>

  <section class="spread">
    <div class="emblem" role="img" aria-label="Radiant cross ornament"></div>
    <h2 class="heading">Man</h2>
    <div class="message size-lg"><p>On the other hand, mankind is corrupt. For example, we are selfish, we are prideful, and we lie.</p></div>
  </section>

  <section class="spread">
    <div class="emblem" role="img" aria-label="Radiant cross ornament"></div>
    <h2 class="heading long">Problem</h2>
    <div class="message size-sm"><p>And there is our big problem: if God is perfect and corruption cannot live with him… and we are corrupt… WE cannot live with God. Our corruption has cut us off from God… now… AND when we die which means we must spend eternity in a place called hell…</p></div>
  </section>

  <section class="spread">
    <div class="emblem" role="img" aria-label="Radiant cross ornament"></div>
    <h2 class="heading">Christ</h2>
    <div class="message size-md">
      <p>But that is not what God wants.</p>
      <p>God loves you so much he gave up his only Son to save you. Jesus Christ died on the cross in our place to pay for our sin and rose again on the 3rd day.</p>
    </div>
  </section>

  <section class="spread">
    <div class="emblem" role="img" aria-label="Radiant cross ornament"></div>
    <h2 class="heading long">Response</h2>
    <div class="message steps">
      <p>So now if anyone:</p>
      <p><b>1.</b> Agrees with God they are corrupt.</p>
      <p><b>2.</b> Believes Jesus Christ will save them.</p>
      <p><b>3.</b> And accepts Him as their personal Lord and Savior, Jesus Christ will forgive their corruption, reconcile them to God, and come and live inside them.</p>
      <p class="call">You can pray to Jesus Christ right now and ask him to save you using the above three steps as your prayer guide.</p>
    </div>
  </section>

</main>
</body>
</html>
```